Business Card Design Project

Need business card for new non profit organization that includes the attached logo in some form.
with this information
Name: Marcel Ashworthy Treff
Title: President & Founder
A: P.O. Box 61537, Portland, Oregon, 97451-6153
E: marc@hollowaytrust.org
E: marc@marctreff.com
P: 1.971.555.0172

Industry/Entity Type
Non Profit

```html
<!DOCTYPE html>
<html lang="en">
<head>
<meta charset="utf-8">
<title>Marcel Ashworthy Treff – Business Card</title>
<link rel="stylesheet" href="https://fonts.googleapis.com/css2?family=Audiowide&family=Arimo:wght@400;700&display=swap">
<style>
  :root {
    --page: #ffffff;
    --red-bright: #d9252b;
    --red-mid: #c21f26;
    --red-deep: #a81b20;
    --name-fill: #f7ec12;
    --name-edge: #111111;
    --rule: #ffffff;
    --title: #ffffff;
    --contact: #25378a;
    --emblem-bg: #ffffff;
    --emblem-text: #1f3a8a;
  }
  * { box-sizing: border-box; margin: 0; padding: 0; }
  html, body {
    width: 1200px; height: 790px; overflow: hidden;
    background: var(--page);
  }
  .card {
    position: absolute; left: 3px; top: 3px;
    width: 1194px; height: 742px;
    overflow: hidden;
    border: 1px solid #7a1616;
    background: linear-gradient(100deg, var(--red-bright) 0%, var(--red-mid) 55%, var(--red-deep) 100%);
    box-shadow: 0 14px 18px -8px rgba(0,0,0,0.45);
  }
  .card__top-band {
    position: absolute; left: 0; top: 27px; width: 100%; height: 216px;
    background: linear-gradient(90deg, rgba(255,255,255,0.55) 0%, rgba(255,255,255,0.5) 55%, rgba(255,255,255,0.35) 100%);
  }
  .card__bottom-band {
    position: absolute; left: 0; top: 570px; width: 100%; height: 172px;
    background: linear-gradient(90deg, rgba(255,255,255,0.97) 0%, rgba(255,255,255,0.85) 30%, rgba(255,255,255,0.35) 55%, rgba(255,255,255,0) 75%);
  }
  .tile {
    position: absolute; width: 160px; height: 156px;
    background: rgba(255, 255, 255, 0.16);
  }
  .emblem {
    position: absolute; left: 38px; top: 44px;
    width: 360px; height: 176px; border-radius: 50%;
    background: var(--emblem-bg);
    box-shadow: 0 0 10px rgba(255,255,255,0.7);
    display: flex; align-items: center; justify-content: center;
  }
  .emblem__name {
    font-family: "Arimo", Arial, sans-serif; font-weight: 700;
    font-size: 36px; color: var(--emblem-text);
  }
  .holder__name {
    position: absolute; left: 0; top: 0;
    width: 1194px; height: 400px;
  }
  .holder__name-text {
    font-family: "Audiowide", "Arial Black", sans-serif;
    font-size: 60px;
    fill: var(--name-fill);
    stroke: var(--name-edge);
    stroke-width: 7px;
    stroke-linejoin: round;
    paint-order: stroke fill;
  }
  .holder__rule {
    position: absolute; left: 96px; top: 378px;
    width: 1032px; height: 5px; background: var(--rule);
  }
  .holder__title {
    position: absolute; left: 355px; top: 395px;
    font-family: "Arimo", Arial, sans-serif;
    font-size: 57px; line-height: 1; color: var(--title); white-space: nowrap;
  }
  .contact {
    position: absolute; left: 47px; top: 587px;
    list-style: none;
    font-family: "Arimo", Arial, sans-serif;
    font-size: 32px; line-height: 36px; color: var(--contact);
    white-space: nowrap;
  }
</style>
</head>
<body>
  <div class="card">
    <div class="card__top-band"></div>
    <div class="tile" style="left:723px; top:44px; background:rgba(150,30,30,0.4)"></div>
    <div class="tile" style="left:895px; top:122px; background:rgba(170,40,40,0.3)"></div>
    <div class="tile" style="left:1070px; top:122px; background:rgba(170,40,40,0.35)"></div>
    <div class="tile" style="left:723px; top:291px"></div>
    <div class="tile" style="left:895px; top:291px"></div>
    <div class="tile" style="left:546px; top:464px; background:rgba(255,255,255,0.08)"></div>
    <div class="tile" style="left:723px; top:464px; background:rgba(255,255,255,0.08)"></div>
    <div class="tile" style="left:898px; top:549px"></div>
    <div class="card__bottom-band"></div>

    <div class="emblem"><span class="emblem__name">Holloway Trust</span></div>

    <svg class="holder__name" viewBox="0 0 1194 400" aria-labelledby="holder-name">
      <text id="holder-name" class="holder__name-text" x="100" y="364" textLength="1026" lengthAdjust="spacingAndGlyphs">MARCEL ASHWORTHY TREFF</text>
    </svg>
    <div class="holder__rule"></div>
    <p class="holder__title">President &amp; Founder</p>

    <ul class="contact">
      <li>P.O. Box 61537, Portland, Oregon, 97451-6153</li>
      <li>marc@hollowaytrust.org</li>
      <li>marc@marctreff.com</li>
      <li>1.971.555.0172</li>
    </ul>
  </div>
</body>
</html>
```